Calm Fern Healthcare- Aged Care and Community Services

Looking for brochure to advertise our services. I will attach a draft that we do not want to use. Looking for graphics that are as natural as possible to present a personalised service. We supply services to aged people and people with disability. Please make it look classy and professional at the same time. I am looking for creativity. I have also attached the logo. Site addresses can be the last page. ideally looking for 2 designs, one A4 and another smaller possibly DL. Looking for creative out of the box thinkers. Thank you.

Target Market(s)

Aged Care service providers, disability service providers and private hospitals

Font styles to use
Serif
Sans Serif
Script

Colors
6b449b
886aae
eea4c8
f59195
fac994
3176b5
0555a3
cedeed
e4daeb

Requirements
Must have
• Targeted imagery, content and contact details
Nice to have
• personal profiles of people happy with our services

```html
<!DOCTYPE html>
<html lang="en">
<head>
<meta charset="utf-8">
<title>Calm Fern Healthcare – Brochure</title>
<link href="https://fonts.googleapis.com/css2?family=Roboto:wght@400;500;700;900&display=swap" rel="stylesheet">
<style>
:root{
  --pink:#e5197e;
  --purple:#4a2a8e;
  --violet:#7c1fa6;
  --ink:#404040;
  --board:#e3e3e3;
  --paper:#f7f7f8;
  --soft:#e4e4e7;
  --white:#ffffff;
}
*{box-sizing:border-box}
html,body{margin:0;padding:0;width:1200px;height:2400px;overflow:hidden;background:var(--board);font-family:'Roboto',sans-serif}
.gradient-defs{position:absolute;width:0;height:0}
.page{position:absolute;width:468px;height:661px;background:var(--paper);overflow:hidden;box-shadow:0 3px 9px rgba(0,0,0,.22)}
.decor{position:absolute;left:0;top:0;width:468px;height:661px}
.photo{position:absolute;border-radius:50%}
.heading{position:absolute;margin:0;font-family:'Roboto',sans-serif;font-weight:700;font-size:19px;line-height:1.08;color:var(--pink);letter-spacing:-.1px}
.rule{position:absolute;width:52px;height:4px;background:var(--pink)}
.body-text{position:absolute;margin:0;font-family:'Roboto',sans-serif;font-size:8.4px;line-height:11px;color:var(--ink);text-align:justify}
.body-text p{margin:0 0 7px}
.lead-text{position:absolute;margin:0;font-family:'Roboto',sans-serif;font-weight:500;font-size:11.2px;line-height:15.6px;color:#222;text-align:justify}
.footer-url{position:absolute;right:29px;bottom:22px;font-family:'Roboto',sans-serif;font-size:7px;font-weight:700;color:#333}
.footer-url span,.cover-web span{color:var(--pink)}

.brand-name{position:absolute;left:340px;top:30px;width:100px;text-align:center;font-family:'Roboto',sans-serif;font-weight:500;font-size:10px;line-height:12px;color:var(--white)}
.brand-name i{display:block;width:14px;height:14px;margin:0 auto 5px;border-radius:50%;background:var(--white)}
.cover-title{position:absolute;left:52px;top:450px;margin:0;font-family:'Roboto',sans-serif;font-weight:900;font-size:31px;line-height:33px;letter-spacing:-.3px}
.cover-title .t1{color:var(--pink);display:block}
.cover-title .t2{color:var(--purple);display:block}
.contact{position:absolute;left:53px;font-family:'Roboto',sans-serif;font-size:9.6px;line-height:11px;color:#222;display:flex;gap:7px;align-items:flex-start}
.contact svg{flex:none;width:11px;height:11px}

.role-list{position:absolute;margin:0;padding:0;list-style:none;font-family:'Roboto',sans-serif;font-size:8.6px;color:#333}
.role-list li{height:14.4px;display:flex;align-items:center;gap:6px}
.tick{width:8px;height:8px;flex:none}

.numbered{position:absolute;display:flex;align-items:center;height:16px}
.numbered b{width:16px;height:16px;border-radius:50%;border:1.6px solid var(--purple);background:var(--white);color:var(--purple);font:700 9px/13px 'Roboto',sans-serif;text-align:center;z-index:1}
.numbered span{margin-left:-2px;height:12px;background:var(--purple);color:var(--white);font:700 10px/12px 'Roboto',sans-serif;padding:0 10px;letter-spacing:.2px}
.benefit-text{position:absolute;left:34px;margin:0;font-family:'Roboto',sans-serif;font-size:8.4px;line-height:11px;color:var(--ink);width:404px}

.dark-quote{position:absolute;border-radius:50%;display:flex;align-items:center;justify-content:center;text-align:center;font:700 8.4px/14.2px 'Roboto',sans-serif;color:var(--white);padding:0 28px}
</style>
</head>
<body>

<svg class="gradient-defs" aria-hidden="true">
  <defs>
    <linearGradient id="ring" x1="0" y1="0" x2="1" y2="1">
      <stop offset="0" stop-color="#e5197e"/>
      <stop offset=".45" stop-color="#7c1fa6"/>
      <stop offset="1" stop-color="#3c2a8f"/>
    </linearGradient>
    <linearGradient id="wave" x1="0" y1="0" x2="1" y2="1">
      <stop offset="0" stop-color="#e5197e"/>
      <stop offset=".5" stop-color="#9b1fa8"/>
      <stop offset="1" stop-color="#4a2a8e"/>
    </linearGradient>
    <linearGradient id="waveDeep" x1="0" y1="1" x2="1" y2="0">
      <stop offset="0" stop-color="#4a2a8e"/>
      <stop offset="1" stop-color="#b21f9c"/>
    </linearGradient>
  </defs>
</svg>

<section class="page cover" style="left:333px;top:126px">
  <svg class="decor" viewBox="0 0 468 661" aria-hidden="true">
    <circle cx="30" cy="104" r="12" fill="var(--soft)"/>
    <circle cx="408" cy="205" r="47" fill="var(--soft)"/>
    <circle cx="383" cy="265" r="13" fill="var(--soft)"/>
    <circle cx="12" cy="424" r="34" fill="var(--soft)"/>
    <circle cx="282" cy="660" r="42" fill="var(--soft)"/>
    <circle cx="400" cy="15" r="95" fill="#4a2a8e"/>
    <line x1="378" y1="70" x2="330" y2="170" stroke="#4a2a8e" stroke-width="48"/>
    <line x1="196" y1="256" x2="399" y2="498" stroke="#4a2a8e" stroke-width="62"/>
    <circle cx="196" cy="256" r="177" fill="url(#ring)"/>
    <circle cx="399" cy="498" r="112" fill="url(#ring)"/>
    <circle cx="196" cy="256" r="148" fill="var(--white)"/>
    <circle cx="399" cy="498" r="88" fill="var(--white)"/>
    <rect x="338" y="603" width="54" height="8" fill="none" stroke="#fff" stroke-width="1.5"/>
    <rect x="416" y="603" width="8" height="8" fill="#fff" transform="rotate(45 420 607)"/>
    <rect x="448" y="603" width="8" height="8" fill="#fff" transform="rotate(45 452 607)"/>
  </svg>
  <div class="brand-name"><i></i>Calm Fern Healthcare</div>
  <div class="photo" style="left:66px;top:126px;width:260px;height:260px;background:radial-gradient(circle at 45% 55%,#e9e6ea 0%,#b6c9a3 45%,#5f8a49 100%)" role="img" aria-label="Carer embracing a smiling senior woman in a wheelchair in a park"></div>
  <div class="photo" style="left:326px;top:425px;width:146px;height:146px;background:linear-gradient(160deg,#5aa7d8 0%,#d9b49a 55%,#f2d34a 100%)" role="img" aria-label="Nurse with stethoscope holding an elderly patient's hands"></div>
  <h1 class="cover-title"><span class="t1">REIMAGINING</span><span class="t2">HEALTHCARE</span></h1>
  <div class="contact" style="top:540px">
    <svg viewBox="0 0 12 12"><path d="M6 0.5a4 4 0 0 1 4 4c0 3-4 7-4 7s-4-4-4-7a4 4 0 0 1 4-4z" fill="var(--purple)"/><circle cx="6" cy="4.5" r="1.5" fill="#fff"/></svg>
    <div>18 Saltbush Road Harlow WA 6100 Australia<br>Level 2, 47 Ember Street<br>Norwood SA 5067 Australia.</div>
  </div>
  <div class="contact" style="top:586px">
    <svg viewBox="0 0 12 12"><circle cx="6" cy="6" r="5.5" fill="var(--purple)"/><path d="M4 3.3l1.2 1.4-.6.8c.4.9 1 1.5 1.9 1.9l.8-.6 1.4 1.2-.7 1c-2.3-.3-4.4-2.4-4.7-4.7z" fill="#fff"/></svg>
    <div>(08) 9000 1234</div>
  </div>
  <div class="contact cover-web" style="top:607px">
    <svg viewBox="0 0 12 12"><g fill="none" stroke="var(--purple)" stroke-width="1"><circle cx="6" cy="6" r="5"/><ellipse cx="6" cy="6" rx="2.2" ry="5"/><path d="M1 6h10M2 3.5h8M2 8.5h8"/></g></svg>
    <div>www.<span>calmfernhealthcare</span>.com.au</div>
  </div>
</section>

<section class="page about" style="left:99px;top:860px">
  <svg class="decor" viewBox="0 0 468 661" aria-hidden="true">
    <path d="M0 470 C40 540 90 580 170 610 C240 636 290 650 320 661 L0 661 Z" fill="url(#wave)"/>
    <path d="M0 540 C60 560 90 620 200 661 L0 661 Z" fill="url(#waveDeep)" opacity=".8"/>
    <path d="M14 485 l4 -3 4 3 4 -3 4 3" fill="none" stroke="#fff" stroke-width="1.2"/>
    <circle cx="26" cy="528" r="4" fill="#c8b8e8"/>
    <circle cx="30" cy="591" r="5" fill="#c8b8e8"/>
    <line x1="358" y1="319" x2="293" y2="524" stroke="#4a2a8e" stroke-width="40"/>
    <circle cx="358" cy="319" r="76" fill="url(#ring)"/>
    <circle cx="358" cy="319" r="64" fill="#fff"/>
    <circle cx="293" cy="524" r="110" fill="url(#ring)"/>
    <circle cx="293" cy="524" r="92" fill="#fff"/>
  </svg>
  <h2 class="heading" style="left:34px;top:30px">ABOUT US</h2>
  <div class="rule" style="left:34px;top:56px"></div>
  <div class="body-text" style="left:34px;top:70px;width:404px">
    <p>Calm Fern Health Care is a perth based staffing solutions providers which thrives to partners with organisations in meeting their continuing resource requirements. We are slowly building a reputation on our responssiveness to client enquiries, whilist meeting our key service deliverables. We work with service providers in Residential Aged Care, Community Supports and Hospitals.</p>
    <p>We believe in the key to building lasting relationships in life to have a willingness and ability to reciprocity which we aim to do by understanding the intricate needs of our client, collaboratively identify problems, help them progress &nbsp;from their current situation, earn trust and thrive for excellence.</p>
    <p>Our vision is to be the most responsive staffing solution provider in WA, whilst sourcing and placing staff that hold strong values which include ethics, accountability, respect, integrity and adaptable. Our mission is to partner with like-minded organisations that genuinely thrive in making a difference, are ethically placed in society have effective governance at the care of their operations.</p>
  </div>
  <h2 class="heading" style="left:34px;top:235px">WHO WE EMPLOY?</h2>
  <div class="rule" style="left:34px;top:262px"></div>
  <div class="body-text" style="left:34px;top:275px;width:208px;text-align:left">We actively source and recruit skills professionals with direct cultural fit to most of our clients. These roles include but are not limited to:</div>
  <ul class="role-list" style="left:34px;top:312px">
    <li><svg class="tick" viewBox="0 0 8 8"><circle cx="4" cy="4" r="4" fill="var(--pink)"/><path d="M2.2 4.1l1.2 1.2 2.4-2.5" fill="none" stroke="#fff" stroke-width="1"/></svg>Registered Nurses</li>
    <li><svg class="tick" viewBox="0 0 8 8"><circle cx="4" cy="4" r="4" fill="var(--pink)"/><path d="M2.2 4.1l1.2 1.2 2.4-2.5" fill="none" stroke="#fff" stroke-width="1"/></svg>Enrolled Nurses</li>
    <li><svg class="tick" viewBox="0 0 8 8"><circle cx="4" cy="4" r="4" fill="var(--pink)"/><path d="M2.2 4.1l1.2 1.2 2.4-2.5" fill="none" stroke="#fff" stroke-width="1"/></svg>Nursing Assistants/ Cares</li>
    <li><svg class="tick" viewBox="0 0 8 8"><circle cx="4" cy="4" r="4" fill="var(--pink)"/><path d="M2.2 4.1l1.2 1.2 2.4-2.5" fill="none" stroke="#fff" stroke-width="1"/></svg>Allied Health Assistants (Physiotherapy &amp; OT)</li>
    <li><svg class="tick" viewBox="0 0 8 8"><circle cx="4" cy="4" r="4" fill="var(--pink)"/><path d="M2.2 4.1l1.2 1.2 2.4-2.5" fill="none" stroke="#fff" stroke-width="1"/></svg>Chefs and Cooks (healthcare experienced)</li>
    <li><svg class="tick" viewBox="0 0 8 8"><circle cx="4" cy="4" r="4" fill="var(--pink)"/><path d="M2.2 4.1l1.2 1.2 2.4-2.5" fill="none" stroke="#fff" stroke-width="1"/></svg>Caterring Staff and Kitchen hands</li>
    <li><svg class="tick" viewBox="0 0 8 8"><circle cx="4" cy="4" r="4" fill="var(--pink)"/><path d="M2.2 4.1l1.2 1.2 2.4-2.5" fill="none" stroke="#fff" stroke-width="1"/></svg>Cleaning and Domestic Assistants</li>
    <li><svg class="tick" viewBox="0 0 8 8"><circle cx="4" cy="4" r="4" fill="var(--pink)"/><path d="M2.2 4.1l1.2 1.2 2.4-2.5" fill="none" stroke="#fff" stroke-width="1"/></svg>Laundry Attendant and</li>
    <li><svg class="tick" viewBox="0 0 8 8"><circle cx="4" cy="4" r="4" fill="var(--pink)"/><path d="M2.2 4.1l1.2 1.2 2.4-2.5" fill="none" stroke="#fff" stroke-width="1"/></svg>many more related professionals</li>
  </ul>
  <div class="photo" style="left:304px;top:265px;width:108px;height:108px;background:linear-gradient(150deg,#ececec 0%,#9cc9c4 45%,#f1d54b 100%)" role="img" aria-label="Nurse helping an elderly man in a wheelchair beside a yellow sofa"></div>
  <div class="dark-quote" style="left:212px;top:443px;width:162px;height:162px;background:radial-gradient(circle at 50% 40%,#3b3b3b 0%,#1c1c1c 100%)" role="img" aria-label="Dark photograph of care staff behind overlaid text">OUR DIVERSE DATABSE OF SKILLED STAFF GIVES YOU THE PLACE OF MIND YOU NEED TO DO WHAT YO DO BEST, LOOK AFTER YOUR CUSTOMERS.</div>
  <div class="footer-url">www.<span>calmfernhealthcare</span>.com.au</div>
</section>

<section class="page believe" style="left:634px;top:860px">
  <svg class="decor" viewBox="0 0 468 661" aria-hidden="true">
    <path d="M177 0 C290 20 370 70 420 140 C445 175 460 205 468 230 L468 0 Z" fill="url(#wave)"/>
    <path d="M300 0 C380 40 440 100 468 170 L468 0 Z" fill="url(#waveDeep)" opacity=".75"/>
    <path d="M450 190 l4 -3 4 3 4 -3 4 3" fill="none" stroke="#fff" stroke-width="1.2"/>
    <circle cx="460" cy="92" r="5" fill="#c8b8e8"/>
    <line x1="140" y1="523" x2="359" y2="477" stroke="#4a2a8e" stroke-width="38"/>
    <circle cx="140" cy="523" r="107" fill="url(#ring)"/>
    <circle cx="140" cy="523" r="92" fill="#fff"/>
    <circle cx="359" cy="477" r="79" fill="url(#ring)"/>
    <circle cx="359" cy="477" r="66" fill="#fff"/>
  </svg>
  <h2 class="heading" style="left:35px;top:44px">WHAT WE BELIEVE</h2>
  <div class="rule" style="left:35px;top:69px;width:82px"></div>
  <p class="lead-text" style="left:35px;top:86px;width:204px">A person who is appreciated, always does more than what is expected. Our staffare at the centre of all our decisions as we are only as good as the peple we hire. If we look after our staff, they will look after our client.</p>
  <h2 class="heading" style="left:35px;top:208px">WHY PARTNER WITH US?</h2>
  <div class="rule" style="left:35px;top:235px;width:82px"></div>
  <div class="numbered" style="left:35px;top:249px"><b>1</b><span>SERVICE DESIGN</span></div>
  <div class="numbered" style="left:244px;top:249px"><b>2</b><span>TECHNOLOGY</span></div>
  <div class="body-text" style="left:35px;top:270px;width:191px">Prior to placing all staff, we esure we have conducted a full client profile to understand your business needs, to end-to-end operations, service delivery, HR and governance. This will enable us to design a service around your specific needs which allows for a seamless integration. We encourage continuity of service delivery which we implement by ensuring the same staff are placed at your sites. Culturally, this enables our staff to build relationships with your teams and customers aloowing for a natural fit.</div>
  <div class="body-text" style="left:244px;top:270px;width:195px;text-align:left">We have integrated our systems with necessary technology as we believe technology is a part of modern day efficiencies. People are our business and nothing can replace human relatioships, interactions or connections, however to effectively enhance these human related characteristics, technology helps us in maximising efficiencies and mimimising error. Our on-boarding and scheduling platforms are automated, further solidifying compliance and managing risk.</div>
  <div class="photo" style="left:56px;top:439px;width:168px;height:168px;background:linear-gradient(150deg,#f2f2f2 0%,#6ab2d9 40%,#f0d244 100%)" role="img" aria-label="Nurse greeting a smiling elderly man seated on a yellow sofa"></div>
  <div class="photo" style="left:301px;top:419px;width:116px;height:116px;background:radial-gradient(circle at 50% 45%,#e7e2dc 0%,#b8a46a 45%,#5d7d3a 100%)" role="img" aria-label="Doctor walking beside an elderly man in a wheelchair in a sunny park"></div>
  <div class="footer-url">www.<span>calmfernhealthcare</span>.com.au</div>
</section>

<section class="page benefits" style="left:99px;top:1590px">
  <svg class="decor" viewBox="0 0 468 661" aria-hidden="true">
    <path d="M0 470 C40 540 90 580 170 610 C240 636 290 650 320 661 L0 661 Z" fill="url(#wave)"/>
    <path d="M0 540 C60 560 90 620 200 661 L0 661 Z" fill="url(#waveDeep)" opacity=".8"/>
    <path d="M14 490 l4 -3 4 3 4 -3 4 3" fill="none" stroke="#fff" stroke-width="1.2"/>
    <circle cx="26" cy="533" r="4" fill="#c8b8e8"/>
    <circle cx="30" cy="596" r="5" fill="#c8b8e8"/>
    <line x1="148" y1="474" x2="325" y2="518" stroke="#4a2a8e" stroke-width="34"/>
    <circle cx="148" cy="474" r="70" fill="url(#ring)"/>
    <circle cx="148" cy="474" r="58" fill="#fff"/>
    <circle cx="325" cy="518" r="98" fill="url(#ring)"/>
    <circle cx="325" cy="518" r="82" fill="#fff"/>
  </svg>
  <h2 class="heading" style="left:34px;top:32px">KEY PARTNERSHIP BENEFITS</h2>
  <div class="rule" style="left:34px;top:58px;width:62px"></div>
  <div class="numbered" style="left:34px;top:75px"><b>1</b><span>SERVICE DESIGN</span></div>
  <p class="benefit-text" style="top:101px">A partnership with Calm Fern will enhance your margins and profitable allowing you to put more money towards initiatives that enables operational excellence.</p>
  <div class="numbered" style="left:34px;top:130px"><b>2</b><span>SERVICE DELIVERY IMPROVEMENTS</span></div>
  <p class="benefit-text" style="top:158px">Enhanced customers choice and flexibility as well as improved customers outcomes.</p>
  <div class="numbered" style="left:34px;top:174px"><b>3</b><span>RISK MANAGEMENT ENHANCEMENTS</span></div>
  <p class="benefit-text" style="top:202px">You have the option of outsourcing workover and cost.</p>
  <div class="numbered" style="left:34px;top:219px"><b>4</b><span>OPERATIONAL EFFICIENCIES</span></div>
  <p class="benefit-text" style="top:247px">Improved operational efficiencies and optimisation of the workforce.</p>
  <h2 class="heading" style="left:34px;top:271px">THE REAL RETURN OF INVESTMENT</h2>
  <div class="rule" style="left:34px;top:296px;width:82px"></div>
  <div class="body-text" style="left:34px;top:311px;width:404px">The more your clients are satisfied, the more they are capable of promoting your brand, speaking highly of your service delivery during accreditation's and ultimately the more they feel you value them as individuals. The Care Standards Council relentlessly seek evidence of compassionate, compliant and effective corporate and clinical governance, by embedding these standards into each policy, process, &nbsp;service implementation to evaluation, the more you will have peace of mind should any regulatory department decides to pay you a visit. We are here to ensure we align to youur standard whilst being adaptable to the changing nature of the industry we operate in.</div>
  <div class="photo" style="left:97px;top:423px;width:102px;height:102px;background:linear-gradient(150deg,#f1ede8 0%,#5da3d4 45%,#e6c9b0 100%)" role="img" aria-label="Smiling nurse with an elderly woman indoors"></div>
  <div class="photo" style="left:251px;top:444px;width:148px;height:148px;background:radial-gradient(circle at 50% 45%,#d6dccb 0%,#8fae6c 50%,#476b33 100%)" role="img" aria-label="Carer and a senior woman in a wheelchair pointing at something in a garden"></div>
  <div class="footer-url">www.<span>calmfernhealthcare</span>.com.au</div>
</section>

<section class="page experiences" style="left:634px;top:1590px">
  <svg class="decor" viewBox="0 0 468 661" aria-hidden="true">
    <path d="M177 0 C290 20 370 70 420 140 C445 175 460 205 468 230 L468 0 Z" fill="url(#wave)"/>
    <path d="M300 0 C380 40 440 100 468 170 L468 0 Z" fill="url(#waveDeep)" opacity=".75"/>
    <path d="M450 192 l4 -3 4 3 4 -3 4 3" fill="none" stroke="#fff" stroke-width="1.2"/>
    <circle cx="460" cy="88" r="5" fill="#c8b8e8"/>
    <line x1="109" y1="339" x2="233" y2="530" stroke="#4a2a8e" stroke-width="40"/>
    <line x1="359" y1="334" x2="233" y2="530" stroke="#4a2a8e" stroke-width="40"/>
    <circle cx="109" cy="339" r="79" fill="url(#ring)"/>
    <circle cx="109" cy="339" r="66" fill="#fff"/>
    <circle cx="359" cy="334" r="81" fill="url(#ring)"/>
    <circle cx="359" cy="334" r="68" fill="#fff"/>
    <circle cx="233" cy="530" r="116" fill="url(#ring)"/>
    <circle cx="233" cy="530" r="98" fill="#fff"/>
  </svg>
  <h2 class="heading" style="left:35px;top:55px">REDESIGNING RESIDENT<br>EXPERIENCES</h2>
  <div class="rule" style="left:35px;top:101px;width:82px"></div>
  <p class="lead-text" style="left:35px;top:118px;width:320px">We value feedback and we consistently seek it as it help us grow. Service Delivery and feedback are a match that cannot be unweeded.</p>
  <h2 class="heading" style="left:35px;top:180px">RETAINING CUSTOMERS &amp;<br>HOW WE GROW</h2>
  <div class="rule" style="left:35px;top:226px;width:82px"></div>
  <div class="photo" style="left:51px;top:281px;width:116px;height:116px;background:linear-gradient(140deg,#eae6e2 0%,#a9b8c9 50%,#d3b6a3 100%)" role="img" aria-label="Doctor and a patient in a bright clinic"></div>
  <div class="photo" style="left:299px;top:274px;width:120px;height:120px;background:linear-gradient(140deg,#dfe6ee 0%,#86b1d4 50%,#e0b437 100%)" role="img" aria-label="Medical team attending a patient in a hospital room"></div>
  <div class="photo" style="left:145px;top:442px;width:176px;height:176px;background:radial-gradient(circle at 55% 45%,#ffffff 0%,#dfe7ef 55%,#a9b9cc 100%)" role="img" aria-label="Doctor in a white coat holding a stethoscope"></div>
  <div class="footer-url">www.<span>calmfernhealthcare</span>.com.au</div>
</section>

</body>
</html>
```